Business Cards & Stationery for a Gold Refiner
Brambleton Assets
Business Cards & Stationery for a Gold Refiner - Jewelry
Creative Brief
Professional
(MUST BE LEFT BLANK)
18 East 52nd Street, Suite 400, New York, NY 10022
(212) 584-6468
info@brambletonassetsllc.example
Hey Designers, We would like for our telephone, fax, and email to be titled with symbols instead of words, e.g. a small telephone symbol next to the phone number and a fax machine next to the fax number. We require blank fields we can fill in, with no symbols, for: NAME, TITLE We require blank fields we can fill in, with symbols, for: CELL NUMBER, EMAIL, WEB ADDRESS Also, and this point is VERY IMPORTANT, we need the final deliverables to include an editable Adobe Illustrator and/or Photoshop file (preferably, Illustrator). We will include the names and titles of our individual employees ourselves, thus we need those sections to be left blank. All fields should be editable. We will not accept the design if it does not include a fully editable file. Our logo was recently completed and we require it to be included in the design. The file should be attached to the contest. We have additional versions of the logo we'd like to be able to swap out at will, however they are all in the same style as the logo provided, so the color scheme of the logo should be utilized throughout. The font should be traditional and corporate in style, and not too stylized or flashy. The logo should be included on the back as well. Thanks Everybody and Good Luck!

```html
<!DOCTYPE html>
<html lang="en">
<head>
<meta charset="utf-8">
<title>Brambleton Assets – Business Card</title>
<link rel="stylesheet" href="https://fonts.googleapis.com/css2?family=Roboto+Condensed:wght@700&family=Roboto:wght@400;500&display=swap">
<style>
  :root {
    --gold: #d4a20e;
    --grey: #8a8a8a;
    --grey-dark: #5b5b5b;
    --ink: #555555;
    --paper: #ffffff;
    --backdrop: #eeeeee;
  }
  * { margin: 0; padding: 0; box-sizing: border-box; }
  html, body {
    width: 1200px; height: 799px; overflow: hidden;
    background: var(--backdrop);
    font-family: "Roboto", Arial, sans-serif;
  }
  .canvas {
    position: relative; width: 1200px; height: 799px;
    display: flex; align-items: center; justify-content: center; gap: 60px;
  }
  .card {
    position: relative; width: 520px; height: 297px; overflow: hidden;
    box-shadow: 0 4px 14px rgba(0,0,0,.12);
  }
  .card--front { background: var(--paper); }
  .card--back {
    background: var(--gold);
    display: flex; flex-direction: column; align-items: center; justify-content: center;
  }

  .corner-bands { position: absolute; left: 0; bottom: 0; width: 520px; height: 297px; }

  .holder { position: absolute; top: 52px; left: 0; width: 100%; text-align: center; padding-left: 110px; }
  .holder__name { color: var(--gold); font-size: 13px; font-weight: 500; }
  .holder__title { color: var(--gold); font-size: 9px; margin-top: 3px; }

  .brand { display: flex; align-items: center; gap: 10px; }
  .brand__mark { width: 34px; height: 34px; background: var(--gold); flex: none; }
  .brand__name {
    font-family: "Roboto Condensed", "Arial Narrow", sans-serif; font-weight: 700;
    font-size: 26px; line-height: 1; text-transform: uppercase; letter-spacing: .5px;
    color: var(--grey-dark); white-space: nowrap;
  }
  .card--front .brand { position: absolute; top: 100px; left: 175px; }
  .card--back .brand__mark { background: var(--paper); width: 44px; height: 44px; }
  .card--back .brand__name { color: var(--paper); font-size: 34px; }

  .contact {
    position: absolute; top: 178px; left: 165px;
    color: var(--ink); font-size: 8.5px; font-style: normal;
  }
  .contact__address { margin-bottom: 7px; }
  .contact__row { display: flex; gap: 18px; margin-bottom: 6px; }
  .contact__item { display: flex; align-items: center; gap: 5px; white-space: nowrap; }
  .contact__icon { width: 10px; height: 10px; flex: none; }

  .web { color: var(--paper); font-size: 11px; margin-top: 10px; letter-spacing: .3px; }
</style>
</head>
<body>
<main class="canvas">
  <section class="card card--front" aria-label="Card front">
    <svg class="corner-bands" viewBox="0 0 520 297" aria-hidden="true">
      <polygon points="0,170 0,205 150,297 205,297" fill="var(--grey)"/>
      <polygon points="0,225 0,297 115,297" fill="var(--gold)"/>
    </svg>

    <div class="holder">
      <p class="holder__name">Dana Whitlock</p>
      <p class="holder__title">President</p>
    </div>

    <div class="brand">
      <span class="brand__mark"></span>
      <span class="brand__name">Brambleton Assets</span>
    </div>

    <address class="contact">
      <p class="contact__address">18 East 52nd Street, Suite 400, New York, NY 10022</p>
      <div class="contact__row">
        <span class="contact__item">
          <svg class="contact__icon" viewBox="0 0 10 10"><circle cx="5" cy="5" r="5" fill="var(--gold)"/><path d="M3.2 2.6l1 1-.6.7c.4.8 1 1.4 1.8 1.8l.7-.6 1 1-.6.9C4.5 7.3 2.7 5.5 2.4 3.2z" fill="#fff"/></svg>
          (212) 584-6468
        </span>
        <span class="contact__item">
          <svg class="contact__icon" viewBox="0 0 10 10"><circle cx="5" cy="5" r="5" fill="var(--gold)"/><rect x="2.8" y="2.5" width="4.4" height="2" fill="#fff"/><rect x="2.3" y="4.8" width="5.4" height="2.6" fill="#fff"/></svg>
          (212) 584-6470
        </span>
      </div>
      <div class="contact__row">
        <span class="contact__item">
          <svg class="contact__icon" viewBox="0 0 10 10"><circle cx="5" cy="5" r="5" fill="var(--gold)"/><rect x="2.5" y="3.2" width="5" height="3.6" fill="#fff"/><path d="M2.5 3.2L5 5.3l2.5-2.1" stroke="var(--gold)" stroke-width=".6" fill="none"/></svg>
          info@brambletonassetsllc.example
        </span>
        <span class="contact__item">
          <svg class="contact__icon" viewBox="0 0 10 10"><circle cx="5" cy="5" r="5" fill="var(--gold)"/><circle cx="5" cy="5" r="2.6" stroke="#fff" stroke-width=".7" fill="none"/><path d="M2.4 5h5.2M5 2.4v5.2" stroke="#fff" stroke-width=".6"/></svg>
          brambletonassetsllc.example
        </span>
      </div>
    </address>
  </section>

  <section class="card card--back" aria-label="Card back">
    <div class="brand">
      <span class="brand__mark"></span>
      <span class="brand__name">Brambleton Assets</span>
    </div>
    <p class="web">brambletonassetsllc.example</p>
  </section>
</main>
</body>
</html>
```